Business Card Design Project

Business and Appointment Card for Medical Practice. On back of card we would like to have: blank line for patient name, Mon-Fri each with a check box next to the day, blank line for appointment date, blank line for appointment time, with option to circle am or pm.

Target Market(s)

Professional Business Associates, as well as function as patient appointment cards (on back side of card)

Industry/Entity Type

Business

Colors

Designer to choose colors to be used in the design.

```html
<!DOCTYPE html>
<html lang="en">
<head>
<meta charset="UTF-8">
<title>Birchwood Medical Group – Appointment Card</title>
<link rel="stylesheet" href="https://fonts.googleapis.com/css2?family=Questrial&display=swap">
<style>
  :root {
    --backdrop: #e4e4e6;
    --card: #ffffff;
    --green: #135e34;
    --red: #8f1c1f;
    --field: #ffffff;
    --label: #ffffff;
  }
  * { margin: 0; padding: 0; box-sizing: border-box; }
  html, body {
    width: 983px; height: 1200px; overflow: hidden;
    background: var(--backdrop);
    font-family: "Questrial", "Century Gothic", sans-serif;
  }
  .canvas { position: relative; width: 983px; height: 1200px; }

  .card { position: absolute; background: var(--card); overflow: hidden; }
  .card--appointment { left: 127px; top: 114px; width: 727px; height: 425px; }
  .card--brand { left: 125px; top: 654px; width: 732px; height: 426px; }

  /* Wordmark */
  .wordmark { position: absolute; display: flex; align-items: center; color: var(--green); }
  .wordmark__dot { flex: none; border-radius: 50%; background: var(--green); }
  .wordmark__name { line-height: 1; text-transform: uppercase; white-space: nowrap; }
  .wordmark__line1 { display: block; letter-spacing: 2px; }
  .wordmark__line2 { display: block; margin-top: 6px; }

  .card--appointment .wordmark { left: 58px; top: 22px; gap: 24px; }
  .card--appointment .wordmark__dot { width: 100px; height: 100px; }
  .card--appointment .wordmark__line1 { font-size: 66px; }
  .card--appointment .wordmark__line2 { font-size: 33px; letter-spacing: 6px; }

  /* Appointment bands */
  .band { position: absolute; left: 0; width: 100%; }
  .band--name { top: 153px; height: 110px; background: var(--green); }
  .band--date {
    top: 263px; height: 127px; background: var(--red);
    display: flex; flex-direction: column; justify-content: center; gap: 20px;
    padding: 0 29px;
  }

  .label { color: var(--label); font-size: 21px; white-space: nowrap; line-height: 1; }
  .field { display: inline-block; background: var(--field); }
  .tickbox { display: inline-block; width: 16px; height: 16px; background: var(--field); }

  .band--name .label { position: absolute; left: 43px; top: 45px; }
  .band--name .field { position: absolute; left: 211px; top: 39px; width: 464px; height: 33px; }

  .row { display: flex; align-items: center; }
  .row--days { gap: 34px; }
  .day { display: flex; align-items: center; gap: 9px; }
  .day .label { font-size: 19px; }

  .row--when { gap: 12px; }
  .field--date { width: 128px; height: 27px; }
  .field--time { width: 100px; height: 27px; margin-right: 8px; }
  .label--time { margin-left: 6px; }
  .label--meridiem { font-size: 19px; letter-spacing: 1px; }

  /* Brand side stripes */
  .stripe { position: absolute; left: 0; width: 100%; }
  .stripe--top-green { top: 0; height: 19px; background: var(--green); }
  .stripe--top-red { top: 19px; height: 15px; background: var(--red); }
  .stripe--bottom-red { top: 390px; height: 15px; background: var(--red); }
  .stripe--bottom-green { top: 405px; height: 21px; background: var(--green); }

  .card--brand .wordmark {
    left: 0; right: 0; top: 34px; height: 356px;
    flex-direction: column; justify-content: center; gap: 16px;
  }
  .card--brand .wordmark__dot { width: 150px; height: 150px; }
  .card--brand .wordmark__name { text-align: center; }
  .card--brand .wordmark__line1 { font-size: 62px; }
  .card--brand .wordmark__line2 { font-size: 32px; letter-spacing: 6px; }
</style>
</head>
<body>
<main class="canvas">

  <section class="card card--appointment" aria-label="Appointment side">
    <div class="wordmark">
      <span class="wordmark__dot" aria-hidden="true"></span>
      <span class="wordmark__name">
        <span class="wordmark__line1">Birchwood</span>
        <span class="wordmark__line2">Medical Group</span>
      </span>
    </div>

    <div class="band band--name">
      <span class="label">Patient Name :</span>
      <span class="field"></span>
    </div>

    <div class="band band--date">
      <div class="row row--days">
        <span class="day"><span class="label">Mon</span><span class="tickbox"></span></span>
        <span class="day"><span class="label">Tue</span><span class="tickbox"></span></span>
        <span class="day"><span class="label">Wed</span><span class="tickbox"></span></span>
        <span class="day"><span class="label">Thu</span><span class="tickbox"></span></span>
        <span class="day"><span class="label">Fri</span><span class="tickbox"></span></span>
      </div>
      <div class="row row--when">
        <span class="label">Appointment Date :</span>
        <span class="field field--date"></span>
        <span class="label label--time">Time :</span>
        <span class="field field--time"></span>
        <span class="label label--meridiem">a.m. / p.m.</span>
      </div>
    </div>
  </section>

  <section class="card card--brand" aria-label="Brand side">
    <span class="stripe stripe--top-green"></span>
    <span class="stripe stripe--top-red"></span>
    <div class="wordmark">
      <span class="wordmark__dot" aria-hidden="true"></span>
      <span class="wordmark__name">
        <span class="wordmark__line1">Birchwood</span>
        <span class="wordmark__line2">Medical Group</span>
      </span>
    </div>
    <span class="stripe stripe--bottom-red"></span>
    <span class="stripe stripe--bottom-green"></span>
  </section>

</main>
</body>
</html>
```